B2B Marketing book cover design for print

We need a book cover design for print. The book is about business to business marketing, based on education. The main concept is that the challenge for industrial marketing, basically is to educate and then attract customers. The book is in spanish: "Vendalia - una ruta para ganar y fidelizar compradores B2B". Which means, "Vendalia - a roadmap to win and retain B2B buyers". The size of the cover is 21 x 14,8 cms. Spine of 2 cms. aprox. The final design should communicate industrial companies and education. We are opened to any color. I'll provide all the text for the cover. It also has 2 book flaps with the photo and brief curriculum of the author and a guest contributor.

Target Market(s)

General managers, CEO, marketing managers, sales managers.

Industry/Entity Type

Marketing

Font styles to use
Serif

Colors

Designer to choose colors to be used in the design.

Requirements
Must have
• 2 book flaps. A taste of mixing industry and education or learning for marketing purpose.
Nice to have
• A look and feel of machinery and engineering. If possible, a rerefence to eCommerce because we also talk about eCommerce for B2B. This are not the elements it "must" have the design, I mean if it's possible to blend something, then great. If not, I'm totally opened to the designer's suggestions.
Should not have
• Lumorix or zentrel references, because they are strongly related to consumer goods marketing, and this books is all about industrial marketing.

```html
<!DOCTYPE html>
<html lang="es">
<head>
<meta charset="utf-8">
<title>Vendalia – Cubierta</title>
<link rel="stylesheet" href="https://fonts.googleapis.com/css2?family=Aldrich&family=EB+Garamond:ital,wght@1,500&display=swap">
<style>
  :root {
    --cover-top: #3a3b3d;
    --cover-bottom: #1d1d1f;
    --gold-light: #f6e7b0;
    --gold-mid: #c9a24a;
    --gold-dark: #7a5a1c;
    --gear-shadow: #1a1408;
    --subtitle: #f2f2f2;
  }
  html, body {
    margin: 0;
    padding: 0;
    width: 960px;
    height: 1200px;
    overflow: hidden;
    background: var(--cover-bottom);
  }
  .cover {
    position: relative;
    width: 960px;
    height: 1200px;
    background: linear-gradient(160deg, var(--cover-top) 0%, #2a2b2d 45%, var(--cover-bottom) 100%);
    overflow: hidden;
  }
  .cover__artwork {
    position: absolute;
    left: 0;
    top: 90px;
    width: 880px;
    height: 480px;
    background:
      radial-gradient(ellipse 38% 42% at 62% 38%, var(--gold-light) 0%, var(--gold-mid) 40%, rgba(122,90,28,0.6) 75%, rgba(0,0,0,0) 100%),
      radial-gradient(ellipse 30% 30% at 30% 22%, var(--gold-mid) 0%, rgba(122,90,28,0.5) 60%, rgba(0,0,0,0) 100%),
      radial-gradient(ellipse 22% 28% at 24% 70%, var(--gold-mid) 0%, var(--gear-shadow) 70%, rgba(0,0,0,0) 100%),
      linear-gradient(90deg, rgba(201,162,74,0.55) 0%, rgba(201,162,74,0) 30%);
  }
  .cover__title {
    position: absolute;
    left: 0;
    right: 0;
    top: 600px;
    margin: 0;
    text-align: center;
    font-family: "Aldrich", sans-serif;
    font-weight: 400;
    font-size: 104px;
    letter-spacing: 2px;
    text-transform: uppercase;
    line-height: 1;
    background: linear-gradient(180deg, var(--gold-light) 0%, var(--gold-mid) 48%, var(--gold-dark) 52%, var(--gold-mid) 100%);
    -webkit-background-clip: text;
    background-clip: text;
    color: transparent;
  }
  .cover__title-initial {
    font-size: 136px;
  }
  .cover__subtitle {
    position: absolute;
    left: 0;
    right: 0;
    top: 800px;
    margin: 0;
    text-align: center;
    font-family: "EB Garamond", serif;
    font-style: italic;
    font-weight: 500;
    font-size: 27px;
    letter-spacing: 2px;
    text-transform: uppercase;
    color: var(--subtitle);
  }
  .cover__subtitle-tag {
    font-size: 42px;
    letter-spacing: 1px;
  }
</style>
</head>
<body>
  <main class="cover">
    <div class="cover__artwork" role="img" aria-label="Engranajes dorados metálicos entrelazados sobre fondo oscuro"></div>
    <h1 class="cover__title"><span class="cover__title-initial">V</span>endalia</h1>
    <p class="cover__subtitle">una ruta para ganar y fidelizar compradores <span class="cover__subtitle-tag">B2B</span></p>
  </main>
</body>
</html>
```